Design graphics and Print for a line of Herb Seeds- Envelope Design

We need a set of herb seed envelopes designed for a new seed line we are launching.
The design will be both front and back

Envelope will be a colored ( green) ) envelope with white text
or a white or cream envelope in all black /and images text. Or can add some colors to the white envelope.

I have attached the die-cut of the seed envelope.
I have attached some images of envelopes I like. Please do not copy, these are just to give you an idea of what I like.

Please feel free to reach out to me if you have any questions.

Thank you

Target Market(s)

The design needs to classic that can translate to 3 different audiences. 1. young parents 2. hip, young single millennial 3. kids

Industry/Entity Type

Ecommerce

Font styles to use
Serif

Requirements
Must have
• Please use the herb - Parsley for the design
Icon, Text or both.

Front side must have:
1.either herb Icon or work Parsley or both- this will be the main attraction
2. company name- Tall Meadow Pantry
3. can use design elements
4. can use my logo on from or back or not at all. I

Backside must have:
1. social media tags
FB, Instagram and Pinterest ( use icons) @tallmeadowpantry

my website: www.tallmeadowpantry.example
this can be on from or back of the envelope.
Should not have
• please stay away from "county" flowery, old fashioned style designs

```html
<!DOCTYPE html>
<html lang="en">
<head>
<meta charset="utf-8">
<title>Parsley Seed Envelope – Tall Meadow Pantry</title>
<link rel="stylesheet" href="https://fonts.googleapis.com/css2?family=Montserrat:wght@400;600&family=Yellowtail&display=swap">
<style>
  :root {
    --sheet-bg: #939498;
    --paper-light: #d2e8c3;
    --paper-mid: #c9e2b7;
    --paper-edge: #bcd9a6;
    --ink-green: #4b8341;
    --brand-green: #8cc63f;
    --ink-grey: #4f5a4c;
    --leaf-dark: #4f9a3c;
    --leaf-light: #9ccc63;
  }
  * { box-sizing: border-box; margin: 0; padding: 0; }
  html, body { width: 787px; height: 1200px; overflow: hidden; background: var(--sheet-bg); }
  .sheet { position: relative; width: 787px; height: 1200px; }
  .abs { position: absolute; }

  .dieline { position: absolute; left: 0; top: 0; width: 787px; height: 600px;
    filter: drop-shadow(4px 8px 8px rgba(0,0,0,.25)); }

  .brand-mark {
    position: absolute; border: 1.5px solid var(--brand-green); border-radius: 50%;
    display: flex; align-items: center; justify-content: center; text-align: center;
    font-family: "Montserrat", sans-serif; font-weight: 600; color: var(--brand-green);
    text-transform: uppercase; letter-spacing: .08em; line-height: 1.25;
  }

  .social-row { position: absolute; display: flex; gap: 7px; transform: translateX(-50%); }
  .social-icon { width: 14px; height: 14px; border: 1px solid var(--ink-grey); border-radius: 50%; }

  .contact-line {
    position: absolute; transform: translateX(-50%); white-space: nowrap;
    font-family: "Montserrat", sans-serif; font-weight: 400; color: var(--ink-grey);
    letter-spacing: .2em;
  }

  .herb-title {
    position: absolute; font-family: "Yellowtail", cursive; color: var(--ink-green);
    line-height: 1; white-space: nowrap;
  }

  .parsley-art {
    position: absolute;
    background: radial-gradient(ellipse at 40% 60%, var(--leaf-dark) 0%, #6eb04a 45%, var(--leaf-light) 75%, rgba(156,204,99,0) 100%);
  }

  .envelope {
    position: absolute; top: 707px; width: 278px; height: 378px;
    background: linear-gradient(180deg, var(--paper-light), var(--paper-mid));
    box-shadow: 4px 8px 12px rgba(0,0,0,.28); overflow: hidden;
  }
  .envelope--back { left: 91px; }
  .envelope--front { left: 402px; }
  .envelope-flap {
    position: absolute; left: 0; top: 0; width: 100%; height: 51px;
    background: var(--paper-light); border-radius: 0 0 14px 14px;
    box-shadow: 0 2px 3px rgba(0,0,0,.12);
  }
  .envelope-seam { position: absolute; left: 0; top: 0; width: 6px; height: 100%; background: var(--paper-edge); }
</style>
</head>
<body>
<main class="sheet">

  <!-- Die-cut layout -->
  <svg class="dieline" viewBox="0 0 787 600" aria-hidden="true">
    <defs>
      <linearGradient id="paper" x1="0" y1="0" x2="0" y2="1">
        <stop offset="0" stop-color="#d2e8c3"/>
        <stop offset="1" stop-color="#c7e0b4"/>
      </linearGradient>
    </defs>
    <path fill="url(#paper)" d="
      M101 175 Q101 157 119 157 L364 157 L364 117 Q364 108 373 108 L608 108 Q617 108 617 117 L617 157
      L659 157 Q668 157 668 166 L668 420 Q668 440 664 460 L664 500 Q664 510 656 512 L617 512
      L617 556 Q617 565 608 565 L373 565 Q364 565 364 556 L364 516 L119 516 Q101 516 101 498 Z"/>
  </svg>

  <div class="brand-mark" style="left:188px; top:284px; width:78px; height:78px; font-size:7.5px;">Tall<br>Meadow<br>Pantry</div>
  <div class="social-row" style="left:225px; top:416px;">
    <span class="social-icon"></span><span class="social-icon"></span><span class="social-icon"></span>
  </div>
  <p class="contact-line" style="left:218px; top:435px; font-size:7.5px;">@tallmeadowpantry</p>
  <p class="contact-line" style="left:225px; top:463px; font-size:7.5px;">www.tallmeadowpantry.example</p>

  <h1 class="herb-title" style="left:412px; top:222px; font-size:66px;">parsley</h1>
  <svg class="abs" style="left:0; top:0;" width="787" height="600" aria-hidden="true">
    <path d="M548 300 C 575 282, 600 300, 648 285" fill="none" stroke="#4b8341" stroke-width="2.5" stroke-linecap="round"/>
  </svg>
  <div class="parsley-art" role="img" aria-label="Watercolour illustration of flat-leaf parsley sprigs"
       style="left:359px; top:302px; width:309px; height:263px; border-radius:0 0 9px 0;"></div>

  <!-- Back of envelope -->
  <section class="envelope envelope--back">
    <span class="envelope-seam"></span>
    <div class="envelope-flap"></div>
    <div class="brand-mark" style="left:96px; top:132px; width:86px; height:86px; font-size:8px;">Tall<br>Meadow<br>Pantry</div>
    <div class="social-row" style="left:139px; top:274px;">
      <span class="social-icon"></span><span class="social-icon"></span><span class="social-icon"></span>
    </div>
    <p class="contact-line" style="left:139px; top:293px; font-size:8px;">@tallmeadowpantry</p>
    <p class="contact-line" style="left:139px; top:324px; font-size:7.5px;">www.tallmeadowpantry.example</p>
  </section>

  <!-- Front of envelope -->
  <section class="envelope envelope--front">
    <h2 class="herb-title" style="left:52px; top:72px; font-size:70px;">parsley</h2>
    <svg class="abs" style="left:0; top:0;" width="278" height="378" aria-hidden="true">
      <path d="M190 148 C 215 130, 240 156, 278 150" fill="none" stroke="#4b8341" stroke-width="2.5" stroke-linecap="round"/>
    </svg>
    <div class="parsley-art" role="img" aria-label="Watercolour illustration of flat-leaf parsley sprigs"
         style="left:0; top:160px; width:278px; height:218px;"></div>
  </section>

</main>
</body>
</html>
```